its a new company based in Christchurch new Zealand building computers ,repairs, upgrades and anything computers for the general public,i like bright happy colours like yellows, greens reds anything that stands out and it needs to communicant trust and security towards my new company,i have no logo yet,

Target Market(s)

target market of all ages

Industry/Entity Type

Building

Contact Information for Business Card

Pixel Harbour Limited,ph-0214862735,email-bluefoxtrail17@mailnest.example,4c marlowe rd,fernvale

```html
<!DOCTYPE html>
<html lang="en">
<head>
<meta charset="utf-8">
<title>Pixel Harbour Limited – Business Card</title>
<link rel="stylesheet" href="https://fonts.googleapis.com/css2?family=Roboto+Condensed:wght@400;700&display=swap">
<style>
  :root {
    --page-bg: #e9e6e1;
    --card-green: #63c13a;
    --card-orange: #f07a22;
    --brand-green: #2fa84a;
    --name-green: #1f7f36;
    --band-purple: #7446b4;
    --band-red: #e2452a;
    --band-green: #1f9a48;
    --band-navy: #124a5e;
    --band-text: #ffffff;
    --tagline-text: #c9f0a6;
    --screen-dark: #1d3c4a;
    --screen-mid: #4a6c78;
  }
  html, body {
    margin: 0;
    padding: 0;
    width: 1200px;
    height: 720px;
    overflow: hidden;
    background: var(--page-bg);
  }
  .canvas {
    position: relative;
    width: 1200px;
    height: 720px;
  }
  .card {
    position: absolute;
    left: 50px;
    top: 46px;
    width: 1100px;
    height: 628px;
    box-shadow: 0 10px 30px rgba(0,0,0,0.18);
  }
  .card svg { display: block; }
  .monogram {
    font-family: "Roboto Condensed", sans-serif;
    font-size: 118px;
    font-weight: 400;
    fill: var(--brand-green);
  }
  .company-name {
    font-family: "Roboto Condensed", sans-serif;
    font-size: 66px;
    font-weight: 400;
    fill: var(--name-green);
  }
  .band-text {
    font-family: "Roboto Condensed", sans-serif;
    font-size: 30px;
    fill: var(--band-text);
  }
  .band-text.email-text { font-size: 26px; }
  .tagline {
    font-family: "Roboto Condensed", sans-serif;
    font-size: 24px;
    fill: var(--tagline-text);
  }
</style>
</head>
<body>
<div class="canvas">
  <div class="card">
    <svg width="1100" height="628" viewBox="0 0 1100 628" xmlns="http://www.w3.org/2000/svg">
      <defs>
        <linearGradient id="screenTone" x1="0" y1="0" x2="1" y2="1">
          <stop offset="0" stop-color="var(--screen-mid)"/>
          <stop offset="0.55" stop-color="var(--screen-dark)"/>
          <stop offset="1" stop-color="#5c7a6a"/>
        </linearGradient>
      </defs>

      <rect class="card-base" width="1100" height="628" fill="var(--card-green)"/>

      <rect class="laptop-photo" x="190" y="22" width="520" height="545" rx="10"
            fill="url(#screenTone)" role="img"
            aria-label="Photo of a laptop showing a tiled start screen"/>

      <polygon class="orange-panel" points="0,58 235,58 640,628 0,628" fill="var(--card-orange)"/>

      <text class="monogram" x="70" y="170">PH</text>

      <text class="company-name" text-anchor="middle" x="290" y="470">Pixel Harbour</text>
      <text class="company-name" text-anchor="middle" x="300" y="548">Limited</text>

      <g class="contact-band phone">
        <rect x="500" y="140" width="330" height="72" fill="var(--band-purple)"/>
        <circle cx="600" cy="176" r="24" fill="#ffffff"/>
        <path d="M591 164 q-4 4 0 12 q5 9 14 14 q7 3 10 -1 l-4 -5 q-3 -2 -5 0 q-5 -2 -9 -8 q2 -3 0 -5 z"
              fill="var(--band-purple)"/>
        <text class="band-text" x="636" y="187">0214862735</text>
      </g>

      <g class="contact-band email">
        <rect x="560" y="214" width="480" height="68" fill="var(--band-red)"/>
        <circle cx="630" cy="248" r="23" fill="#ffffff"/>
        <rect x="618" y="239" width="24" height="17" fill="none" stroke="var(--band-red)" stroke-width="2.5"/>
        <polyline points="618,239 630,249 642,239" fill="none" stroke="var(--band-red)" stroke-width="2.5"/>
        <text class="band-text email-text" x="664" y="257" textLength="358" lengthAdjust="spacingAndGlyphs">bluefoxtrail17@mailnest.example</text>
      </g>

      <g class="contact-band address">
        <rect x="520" y="288" width="540" height="68" fill="var(--band-green)"/>
        <circle cx="700" cy="322" r="23" fill="#ffffff"/>
        <polygon points="700,308 686,321 690,321 690,334 710,334 710,321 714,321" fill="var(--band-green)"/>
        <rect x="697" y="325" width="6" height="9" fill="#ffffff"/>
        <text class="band-text" x="736" y="333">4c marlowe rd, fernvale</text>
      </g>

      <g class="services-band">
        <rect x="545" y="420" width="540" height="62" fill="var(--band-navy)"/>
        <text class="tagline" x="560" y="459" textLength="510" lengthAdjust="spacingAndGlyphs">We're Specialized In: Building Computers, Repairs, Upgrades &amp; more</text>
      </g>
    </svg>
  </div>
</div>
</body>
</html>
```